Menu design for a modern Pizza restaurant

We need a menu design which is visually attractive but also user friendly.
We want it to be A3 but fold in just like the Tonk'd menu attached.
We also want colourful and fun like our branding is.
I have attached another menu example from Ul Pizza which is laid out very well but needs colour.
Also attached is Merno menu which we like the design of, just needs colour.
Attached is our imagery and logo.
And lastly is our menu attached.
We really need it in 24 hours if possible.

Target Market(s)

All Pizza eaters in our area

Industry/Entity Type

Hospitality

Requirements
Must have
• Bold, colourful and fun

```html
<!DOCTYPE html>
<html lang="en">
<head>
<meta charset="utf-8">
<title>Crust Works Menu</title>
<link rel="stylesheet" href="https://fonts.googleapis.com/css2?family=Oswald:wght@500;700&family=Lato:wght@400;700;900&display=swap">
<style>
:root{
  --paper:#fff8ec;
  --paper-deep:#ffeccc;
  --ink:#2b2b2b;
  --rule:#2b2b2b;
  --red:#e0322b;
  --orange:#f58a1f;
  --yellow:#ffd23f;
  --green:#2f9e55;
  --box:#fff1bf;
  --white:#ffffff;
  --muted:#c4271f;
}
*{box-sizing:border-box;margin:0;padding:0}
html,body{width:850px;height:1200px;overflow:hidden}
body{background:var(--paper);color:var(--ink);font-family:"Lato",Arial,sans-serif;position:relative}

.backdrop{position:absolute;inset:0;background:radial-gradient(circle at 20% 25%,var(--paper-deep) 0,transparent 40%),radial-gradient(circle at 80% 70%,#ffe3d6 0,transparent 45%),radial-gradient(circle at 75% 15%,#e6f5e3 0,transparent 35%),radial-gradient(circle at 20% 85%,#fff0c4 0,transparent 40%)}

.edge{position:absolute;left:0;width:850px;height:6px;background:var(--red)}
.edge-top{top:0}.edge-bottom{bottom:0;height:8px}
.fold-v{position:absolute;left:424px;top:30px;height:1150px;border-left:1px dashed var(--orange)}
.fold-h{position:absolute;top:598px;left:0;width:850px;border-top:1px dashed var(--orange)}

.section{position:absolute;left:26px;width:388px}
.section.right{left:436px}
.head{border-top:3px solid var(--rule);border-bottom:1.5px dashed var(--rule);display:flex;align-items:center;justify-content:space-between;height:50px}
.head h2{font-family:"Oswald",Impact,sans-serif;font-weight:700;font-size:36px;letter-spacing:-.5px;line-height:1;color:var(--red);transform:scaleY(1.08)}
.head .price{font-size:16px;color:var(--ink)}
.head .price b{font-weight:900;color:var(--green)}

.pizza-grid{display:grid;grid-template-columns:188px 188px;column-gap:12px;margin-top:10px}
.dish{margin-bottom:12px}
.dish h3{font-weight:900;font-size:10.5px;color:var(--green);text-transform:uppercase;margin-bottom:1px}
.dish p{font-size:10.5px;line-height:13.8px;text-align:justify}

.item{margin-top:10px}
.item h3{font-weight:900;font-size:14px;color:var(--green);text-transform:uppercase}
.item p{font-size:14.5px;line-height:18.5px;text-align:justify}

.sides{margin-top:10px}
.side-row{display:flex;justify-content:space-between;border:1px dotted var(--orange);background:var(--box);padding:3px 9px;font-weight:900;font-size:14px;margin-bottom:4px;color:var(--ink)}
.side-row span:last-child{color:var(--red)}
.cta{margin-top:12px;background:var(--green);color:var(--white);font-weight:900;font-size:14px;text-align:center;height:37px;line-height:37px}

.bases{list-style:none;margin-top:12px}
.bases li{font-size:14px;line-height:18.5px;padding-left:18px;position:relative;margin-bottom:12px}
.bases li::before,.opts li::before{content:"";position:absolute;left:2px;top:6px;width:5px;height:5px;background:var(--orange);transform:rotate(45deg)}
.bases b{font-weight:900;color:var(--green)}
.sub{border-bottom:1.5px dashed var(--rule);margin-top:8px;height:35px;display:flex;align-items:flex-end;padding-bottom:2px}
.sub h3{font-family:"Oswald",Impact,sans-serif;font-weight:700;font-size:23px;line-height:1;letter-spacing:-.3px;color:var(--red);transform:scaleY(1.08)}
.opts{display:grid;grid-template-columns:133px 133px 122px;list-style:none;margin-top:8px}
.opts ul{list-style:none}
.opts li{position:relative;padding-left:18px;font-size:14px;line-height:18.4px;padding-right:4px}

.pricing{margin-top:14px}
.pricing .side-row{margin-bottom:3px}

.brand{position:absolute;left:438px;top:1046px;width:384px;height:120px;background:var(--red);display:flex;align-items:center;justify-content:center}
.brand span{font-family:"Oswald",Impact,sans-serif;font-weight:700;font-size:44px;color:var(--white);letter-spacing:1px}
</style>
</head>
<body>
<div class="backdrop" role="img" aria-label="Faint repeating pattern of pizza slices and hearts across the menu"></div>
<div class="edge edge-top"></div>
<div class="fold-v"></div>
<div class="fold-h"></div>

<section class="section" style="top:30px">
  <div class="head"><h2>PIZZA</h2><span class="price">11 INCH <b>$15</b> &nbsp;/ &nbsp;13 INCH <b>$20</b></span></div>
  <div class="pizza-grid">
    <div>
      <div class="dish"><h3>New York Buffalo</h3><p>Tomato base, rudys buffalo marinated chicken, foir de latte, fresh tomato, red onion, smoked paprika, chilli flakes, and blue cheese sauce.</p></div>
      <div class="dish"><h3>Duck and Nectarine</h3><p>Hoisin base, roasted duck, fresh nectarine, foir de latte, broccoli</p></div>
      <div class="dish"><h3>Sopressa</h3><p>Tomato base, sopressa, pesto, roasted capsicum, fior de latte, cracked black pepper, goat cheese</p></div>
      <div class="dish"><h3>Capricciosa</h3><p>Tomato, ham, mushroom, olives, artichoke, fior de latte, white anchovies,</p></div>
      <div class="dish"><h3>Tropical</h3><p>Tomato base, mozzarella, fresh sliced tomato, fresh pineapple, ham, fior de latte</p></div>
      <div class="dish"><h3>Margherita</h3><p>Tomato base, fresh sliced tomato, scarmoza bianca, fior de latte fresh basil leaves,</p></div>
      <div class="dish"><h3>Mushroom Deluxe</h3><p>Mushroom &amp; truffle duxelle base, confit onions, buffalo mozzarella, thyme, black pepper, field mushroom</p></div>
      <div class="dish"><h3>Carnivore</h3><p>Bbq, beef, bacon, chicken, sopressa, onion, capsicum, tomato, mozzarella</p></div>
    </div>
    <div>
      <div class="dish"><h3>Formaggio Amore</h3><p>Buffalo mozzarella, gorgonzola, fior di latte, parmesan, sage.</p></div>
      <div class="dish"><h3>Garlic Pizza</h3><p>Confit garlic, buffalo mozzarella, fresh garlic, rosemary, extra virgin olive oil, sea salt black pepper,</p></div>
      <div class="dish"><h3>Sage and Pumpkin</h3><p>Extra virgin olive oil, pumpkin, gorgonzola, scarmoza bianca, pine nuts, fior de latte, sage</p></div>
      <div class="dish"><h3>Prosciutto</h3><p>Tomato base, fresh tomato, fresh basil, fior di latte, prosciutto, rocket, garlic oil, buffalo mozzarella</p></div>
      <div class="dish"><h3>Lamb</h3><p>Tomato base, roasted capsicum, eggplant, sun dried tomatoes, lamb, red onion, garlic yogurt, and rocket.</p></div>
      <div class="dish"><h3>Veg Your Heart Out</h3><p>Tomato base, roasted capsicum, broccoli, eggplant, zucchini, mushrooms, onion confit, kale, mozzarella, fior di latte, garlic oil</p></div>
      <div class="dish"><h3>Falafel</h3><p>Falafel, tomato, red onion, zucchini, capsicum, olives, goat cheese, garlic yogurt</p></div>
      <div class="dish"><h3>Pepperoni</h3><p>Calabrese salami, cherry tomato, goats cheese, mozzarella</p></div>
    </div>
  </div>
</section>

<section class="section right" style="top:30px">
  <div class="head"><h2>SALADS</h2><span class="price">/ &nbsp;<b>$14</b></span></div>
  <div class="item"><h3>Couscous and Lamb Salad</h3><p>Pearl couscous, cumin, coriander, cashew, mint, baby spinach, zartar spiced lamb, labneh</p></div>
  <div class="item"><h3>Kale &amp; Broccoli</h3><p>Broccoli, kale, Spanish onion, almonds, carrot, coriander, nectarine, vinocotto</p></div>
</section>

<section class="section right" style="top:223px">
  <div class="head"><h2>PASTA</h2><span class="price">/ &nbsp;<b>$14</b></span></div>
  <div class="item"><h3>Gnocchi</h3><p>Choice of sauce; Leek &amp; gorgonzola, rose', pumpkin &amp; spinach, Napoli</p></div>
</section>

<section class="section right" style="top:351px">
  <div class="head"><h2>SIDES</h2></div>
  <div class="sides">
    <div class="side-row"><span>Chips &amp; Aioli</span><span>$5</span></div>
    <div class="side-row"><span>Garlic Baggett</span><span>$5</span></div>
    <div class="side-row"><span>Buffalo chicken wings &amp; blue cheese sauce</span><span>$12</span></div>
    <div class="side-row"><span>Meat balls stuffed with fior de latte</span><span>$8</span></div>
  </div>
  <div class="cta">Your own Works; Build your own Pizza</div>
</section>

<section class="section" style="top:616px">
  <div class="head"><h2>BASE OPTIONS</h2></div>
  <ul class="bases">
    <li><b>REGULAR -</b> Vegetarian &amp; vegan friendly.</li>
    <li><b>GLUTEN FREE</b></li>
    <li><b>SUPER FOOD BASE -</b> Flax seed, Quinoa, wheat germ, kale, wholemeal, (High protein, High fibre, High nutrient)</li>
  </ul>
  <div class="sub"><h3>BASE</h3></div>
  <div class="opts">
    <ul><li>Tomato</li><li>Pesto</li></ul>
    <ul><li>Hoisin</li><li>BBQ</li></ul>
    <ul><li>Olive oil</li></ul>
  </div>
  <div class="sub"><h3>DAIRY</h3></div>
  <div class="opts">
    <ul><li>Fior de latte</li><li>Scarmoza Bianca</li></ul>
    <ul><li>Gorgonzola</li><li>Buffalo mozzarella</li></ul>
    <ul><li>Parmesan</li><li>Goats cheese</li><li>Eggs</li></ul>
  </div>
  <div class="sub"><h3>FRUIT &amp; VEG</h3></div>
  <div class="opts">
    <ul><li>Broccoli</li><li>Kale</li><li>Capsicum</li><li>Tomato</li><li>Cherry tomatoes</li><li>Olives</li><li>Pineapple</li></ul>
    <ul><li>Red onion</li><li>Caramelised onion</li><li>Artichoke</li><li>Zucchini</li><li>Carrot</li><li>Coriander</li><li>Nectarine</li></ul>
    <ul><li>Mushroom</li><li>Chilli flakes</li><li>Fresh chilli</li><li>Sun dried tomato</li><li>Egg plant</li><li>Basil</li><li>Baby spinach</li></ul>
  </div>
</section>

<section class="section right" style="top:616px">
  <div class="head"><h2>PIZZA PRICING</h2></div>
  <div class="pricing">
    <div class="side-row"><span>Kids</span><span>$5</span></div>
    <div class="side-row"><span>Lunch Special</span><span>$10</span></div>
    <div class="side-row"><span>Regular 11”</span><span>$15</span></div>
    <div class="side-row"><span>Share 13”</span><span>$20</span></div>
  </div>
  <div class="sub"><h3>PROTEIN</h3></div>
  <div class="opts">
    <ul><li>Beef</li><li>Chicken</li><li>Duck</li><li>Lamb</li></ul>
    <ul><li>Bacon</li><li>Calabrese salami Prosciutto</li></ul>
    <ul><li>Sopressa</li><li>Ham</li><li>Anchovies</li></ul>
  </div>
  <div class="sub"><h3>SAUCES</h3></div>
  <div class="opts">
    <ul><li>Tomato</li><li>BBQ</li><li>Mayonnaise</li><li>Aioli</li></ul>
    <ul><li>Dill aioli</li><li>Garlic</li><li>Blue cheese</li></ul>
    <ul><li>Hot sauce</li><li>Mustard</li><li>Siracha Chilli</li></ul>
  </div>
</section>

<div class="brand"><span>CRUST WORKS</span></div>

<div class="edge edge-bottom"></div>
</body>
</html>
```